Quillmark Audio 25th Anniversary Concert

I need a concert poster designed (8.5 x 14) for an upcoming event. Ideally, I would also like to have some digital versions I can post online (Facebook, Twitter, etc.) Check out this Facebook page for ideas: https://www.facebook.com/QuillmarkAudio/
The time, date and location of the event are as follows: Friday, November 24, 2017 at 8:00PM at Gorman's Loft, 2465 Presley Orchard Ln, Salem, VA 24153

Target Market(s)

This poster will be posted in the city where the event is taking place - the target market is individuals who would attend a concert featuring regional bands from the 1990s.

Requirements
Must have
• Feature all of the information in a format that is consistent with the uploaded files and Facebook page.
Nice to have
• As you can see all of the files are in black and white/grayscale. Some color is fine, but bold colors probably don't work.

```html
<!DOCTYPE html>
<html lang="en">
<head>
<meta charset="utf-8">
<title>Quillmark Audio 25th Anniversary Poster</title>
<link rel="stylesheet" href="https://fonts.googleapis.com/css2?family=Anton&family=Staatliches&family=Cinzel:wght@400&family=Rye&family=Courgette&family=Archivo+Black&display=swap">
<style>
  :root {
    --mauve: #a58a87;
    --label: #bfa19c;
    --page: #ffffff;
    --ink: #2b2928;
    --ink-soft: #4a4644;
    --paper: #dcdad6;
    --paper-shade: #c9c6c1;
    --header-box: #e8e6e3;
    --white: #f6f5f3;
  }
  html, body {
    margin: 0;
    padding: 0;
    width: 1200px;
    height: 1200px;
    overflow: hidden;
    background: var(--page);
  }
  .board {
    position: relative;
    width: 1200px;
    height: 1200px;
    background: var(--page);
  }
  .board__band {
    position: absolute;
    left: 772px;
    top: 0;
    width: 428px;
    height: 1200px;
    background: var(--mauve);
  }
  .label {
    position: absolute;
    color: var(--label);
    margin: 0;
  }
  .label--script {
    font-family: "Courgette", cursive;
    font-size: 38px;
    left: 44px;
  }
  .label--client {
    font-family: "Staatliches", sans-serif;
    font-size: 74px;
    line-height: 72px;
    left: 0;
    width: 430px;
    text-align: center;
    top: 396px;
    letter-spacing: 1px;
    text-shadow: 2px 2px 0 #e6d8d5;
  }
  .label--size {
    font-family: "Staatliches", sans-serif;
    font-size: 66px;
    left: 0;
    width: 430px;
    text-align: center;
    top: 748px;
    text-shadow: 2px 2px 0 #e6d8d5;
  }
  .poster {
    position: absolute;
    left: 454px;
    top: 90px;
    width: 620px;
    height: 1020px;
    box-shadow: 4px 6px 14px rgba(0,0,0,0.35);
  }
  .poster svg { display: block; }
</style>
</head>
<body>
<main class="board">
  <div class="board__band"></div>

  <p class="label label--script" style="top:318px;">Poster Design for:</p>
  <p class="label label--client">Quillmark<br>Audio</p>
  <p class="label label--script" style="top:648px;">Dimensions:</p>
  <p class="label label--size">8,5x14”</p>

  <section class="poster">
    <svg width="620" height="1020" viewBox="0 0 620 1020" xmlns="http://www.w3.org/2000/svg">
      <defs>
        <linearGradient id="nightFair" x1="0" y1="0" x2="0" y2="1">
          <stop offset="0" stop-color="#c9c6c3"/>
          <stop offset="0.2" stop-color="#6e6966"/>
          <stop offset="0.45" stop-color="#4a4542"/>
          <stop offset="0.75" stop-color="#2e2b29"/>
          <stop offset="1" stop-color="#3a3735"/>
        </linearGradient>
      </defs>

      <!-- background scene -->
      <rect class="poster__scene" x="0" y="0" width="620" height="1020" fill="url(#nightFair)" role="img" aria-label="Aerial night photograph of a fairground with a lit Ferris wheel"/>

      <!-- dotted frame -->
      <rect x="14" y="14" width="592" height="992" fill="none" stroke="#bdb9b6" stroke-width="2.5" stroke-dasharray="1 5" stroke-linecap="round"/>

      <!-- header: client name -->
      <g class="poster__title">
        <rect x="30" y="30" width="300" height="92" fill="var(--header-box)"/>
        <rect x="338" y="30" width="252" height="92" fill="var(--header-box)"/>
        <text x="180" y="108" text-anchor="middle" font-family="Anton, sans-serif" font-size="80" fill="#858180" textLength="280" lengthAdjust="spacingAndGlyphs">QUILLMARK</text>
        <text x="464" y="108" text-anchor="middle" font-family="Anton, sans-serif" font-size="80" fill="#a4a09e" textLength="232" lengthAdjust="spacingAndGlyphs">AUDIO</text>
      </g>

      <!-- header: anniversary -->
      <g class="poster__anniversary">
        <rect x="30" y="134" width="148" height="92" fill="var(--white)"/>
        <rect x="194" y="134" width="396" height="92" fill="var(--white)"/>
        <text x="104" y="212" text-anchor="middle" font-family="Anton, sans-serif" font-size="78" fill="var(--ink)" textLength="134" lengthAdjust="spacingAndGlyphs">25TH</text>
        <text x="392" y="212" text-anchor="middle" font-family="Anton, sans-serif" font-size="78" fill="var(--ink)" textLength="378" lengthAdjust="spacingAndGlyphs">ANNIVERSARY</text>
      </g>

      <!-- client name in place of mark -->
      <g class="poster__brand">
        <circle cx="310" cy="422" r="118" fill="none" stroke="var(--white)" stroke-width="2"/>
        <text x="310" y="440" text-anchor="middle" font-family="Cinzel, serif" font-size="54" fill="var(--white)" textLength="520" lengthAdjust="spacingAndGlyphs">QUILLMARK AUDIO</text>
      </g>

      <!-- date -->
      <text class="poster__date" x="38" y="634" font-family="Anton, sans-serif" font-size="58" fill="var(--white)" textLength="546" lengthAdjust="spacingAndGlyphs">FRIDAY, NOVEMBER 24, 2017</text>

      <!-- lineup -->
      <g class="poster__lineup" fill="var(--white)">
        <text x="38" y="718" font-family="'Archivo Black', sans-serif" font-size="50" textLength="218" lengthAdjust="spacingAndGlyphs">GRAVEL</text>
        <text x="38" y="770" font-family="Cinzel, serif" font-size="38" textLength="312" lengthAdjust="spacingAndGlyphs">NIGHTJARS</text>
        <text x="38" y="830" font-family="Rye, serif" font-size="44" textLength="282" lengthAdjust="spacingAndGlyphs">Hollow Lantern</text>
      </g>

      <!-- time -->
      <text class="poster__time" x="414" y="760" font-family="Anton, sans-serif" font-size="66" fill="var(--white)" stroke="var(--ink)" stroke-width="1" textLength="150" lengthAdjust="spacingAndGlyphs">8:00PM</text>

      <!-- torn paper footer -->
      <path class="poster__paper" d="M0 902 L20 896 L44 900 L70 888 L96 894 L120 884 L150 890 L176 880 L204 886 L232 872 L262 876 L290 862 L318 868 L344 850 L368 856 L396 838 L420 832 L446 842 L470 826 L496 834 L520 818 L546 832 L572 822 L598 836 L620 830 L620 1020 L0 1020 Z" fill="var(--paper)"/>
      <path d="M0 902 L20 896 L44 900 L70 888 L96 894 L120 884 L150 890 L176 880 L204 886 L232 872 L262 876 L290 862 L318 868 L344 850 L368 856 L396 838 L420 832 L446 842 L470 826 L496 834 L520 818 L546 832 L572 822 L598 836 L620 830" fill="none" stroke="#f2f1ef" stroke-width="3"/>

      <!-- admission -->
      <g class="poster__admission">
        <rect x="396" y="870" width="122" height="32" fill="var(--ink-soft)"/>
        <rect x="524" y="870" width="56" height="32" fill="var(--ink-soft)"/>
        <text x="457" y="895" text-anchor="middle" font-family="Anton, sans-serif" font-size="26" fill="var(--paper)" textLength="112" lengthAdjust="spacingAndGlyphs">ADMISSION:</text>
        <text x="552" y="895" text-anchor="middle" font-family="Anton, sans-serif" font-size="26" fill="var(--paper)" textLength="48" lengthAdjust="spacingAndGlyphs">FREE</text>
      </g>

      <!-- venue -->
      <g class="poster__venue" font-family="Oswald, 'Anton', sans-serif" font-size="30" fill="var(--ink)" text-anchor="middle">
        <text x="310" y="948" textLength="540" lengthAdjust="spacingAndGlyphs">GORMAN'S LOFT, 2465 PRESLEY ORCHARD</text>
        <text x="310" y="986" textLength="300" lengthAdjust="spacingAndGlyphs">LN, SALEM, VA 24153</text>
      </g>
    </svg>
  </section>
</main>
</body>
</html>
```